New Website Announcement

We need a flyer to announce our new website to customers and prospective clients. The website will be launching soon, but I can provide a detailed outline in PDF form with copy and imagery to serve as inspiration for this design.

I would like a postcard size document that can be mailed in an envelope (no need for postcard style mailer info on 1 side)

About my company:

Clearwater Lantern Group is a new breed of marketing consulting agency built for the next frontier of consumer learning. Social interaction will be at the heart of great insights going forward – in how consumers engage with brands and in how organizations socialize what they learn to gain competitive advantage.
By fusing innovative insights techniques, technology and compelling graphic design-based reporting, we ensure results get noticed and make an impact.

contact info that can also be included:

Email: morgan@clearwater-lantern.com

Phone: 518-732-6148

New High Res logo file has been added. (.ai)

Thanks

Reason: Giving more time next week for submissions. This project has been committed. Thanks !

Attention all designers submitting a design for this project. Please keep in mind a few important details about this project.

1. Remember that the main objective of this postcard is to announce my new website.

2. Please be sure to read the brief for the copy I would like on each side. You can be creative in how it is displayed, but I need this key information somewhere. All other copy on the attached files is for your background only.

3. Please do not submit overly simple designs that just take the images I provided and overlay a text box with my copy. I could easily do this myself in PowerPoint in 5 minutes.

4. Remember that the design should be edgy and modern but needs to be professional and speak to a business audience.

Please submit any questions. Thank you for your submissions. 

Morgan

Illustrator high res logo file now correctly uploaded. Thanks.

Target Market(s)

senior level marketing and research clients at large companies and agencies

Industry/Entity Type

Marketing

Requirements
Must have
• Main message:

Need an engaging way to tell customers and prospective clients that we have a new website and that they should come visit us online to learn more about out services, check out case studies and read about our exciting partnerships.

COPY TO USE - UPDATED

Side 1:
(logo)
Introducing Clearwater Lantern Group

Let’s talk about taking research out of the dark ages.

Visit our newly launched website to learn how and get in touch.

www.clearwater-lantern.com

Side 2
Logo
followed by tagline:
Consumer insights that get noticed.
A leading-edge marketing partnership that really works.

Additional text to use on Side 2:
How we can help...

Think of us as your go-to resource for identifying and incorporating the most innovative and exciting techniques into your research programs. We carefully curate and develop close partnerships with the best of the best - from online qualitative research and mobile ethnography to social media listening and fresh takes on concept testing, we can guide the way.

Plus, we believe that socializing consumer learning is just as critical as gathering it.By taking insights deliverables to the next level – through infographics, videos, magazines,interactive profiles and so much more – we are getting stakeholders excited to engage with research and inspired to take action because of it.
It’s a new way to look at insights from a new type of partner. And, it’s a new way to get the most from your research dollars.
Nice to have
• could incorporate our website main image of the lamp on white brick background which is attached, but not 100% mandatory.
Should not have
• - should not be too playful or young, but needs to be modern and design focused

- should not be cluttered or overly 'salesy'

- needs to be upscale and elegant / compelling and aligned with the look and feel of the website imagery (see attached)

```html
<!DOCTYPE html>
<html lang="en">
<head>
<meta charset="utf-8">
<title>Clearwater Lantern Group – Website Launch Postcard</title>
<link href="https://fonts.googleapis.com/css2?family=Lato:ital,wght@0,400;0,700;0,900;1,700;1,900&display=swap" rel="stylesheet">
<style>
  :root {
    --stage: #252627;
    --brand-blue: #1f6fc6;
    --deep-blue: #0d3f8f;
    --ink: #1b1b1b;
    --paper: #ffffff;
    --brick-light: #e9e9e7;
    --brick-mid: #c9c9c6;
    --brick-dark: #9d9d9a;
    --bar-black: #0c0c0c;
  }
  * { box-sizing: border-box; margin: 0; padding: 0; }
  html, body {
    width: 1200px; height: 760px; overflow: hidden;
    background: var(--stage);
    font-family: "Lato", Arial, sans-serif;
  }
  .stage {
    position: relative; width: 1200px; height: 760px;
    display: flex; align-items: center; justify-content: center; gap: 40px;
  }
  .postcard {
    position: relative; width: 560px; height: 376px; overflow: hidden;
    background: var(--brick-light);
    box-shadow: 0 10px 30px rgba(0,0,0,.55);
  }
  .backdrop { position: absolute; inset: 0; }
  .backdrop--front {
    background: radial-gradient(ellipse at 30% 25%, #fafafa 0%, var(--brick-light) 35%, var(--brick-mid) 75%, var(--brick-dark) 100%);
  }
  .backdrop--back {
    background: linear-gradient(180deg, var(--brick-mid) 0%, var(--brick-light) 40%, #f3f3f2 100%);
  }
  .lamp-area {
    position: absolute; left: 20px; top: 20px; width: 180px; height: 300px;
    background: radial-gradient(ellipse at 60% 20%, rgba(255,255,255,.7), rgba(255,255,255,0) 70%);
  }

  /* brand name lockup */
  .brand {
    position: absolute; color: var(--brand-blue);
    font-weight: 900; text-transform: uppercase;
    line-height: 1; letter-spacing: .5px;
  }
  .brand--front { right: 30px; top: 24px; font-size: 30px; text-align: right; }
  .brand--back { right: 26px; bottom: 26px; font-size: 27px; text-align: right; }

  /* speech bubble */
  .bubble { position: absolute; left: 80px; top: 112px; width: 200px; height: 100px; }
  .bubble__text {
    position: absolute; left: 100px; top: 128px; width: 170px;
    font-size: 10.5px; font-weight: 700; color: var(--ink);
    text-align: center; line-height: 1.2;
  }
  .bubble__text em { color: var(--brand-blue); font-weight: 900; font-size: 13px; font-style: italic; }

  /* about banner */
  .about-banner { position: absolute; left: 140px; top: 168px; width: 408px; height: 156px; }
  .about {
    position: absolute; left: 168px; top: 184px; width: 360px;
    color: var(--paper); text-align: center;
  }
  .about__title { font-size: 18px; font-weight: 700; margin-bottom: 6px; padding-left: 60px; text-align: left; }
  .about__body { font-size: 9.6px; line-height: 1.32; }

  .contact-front {
    position: absolute; left: 16px; bottom: 14px;
    font-size: 10.5px; font-weight: 700; color: var(--ink); line-height: 1.45;
  }
  .launch-note {
    position: absolute; right: 14px; bottom: 26px; width: 200px;
    font-size: 10px; font-style: italic; font-weight: 700; text-align: right; color: var(--ink);
    line-height: 1.2;
  }
  .url-bar {
    position: absolute; right: 0; bottom: 0; width: 210px; height: 20px;
    background: var(--bar-black); color: var(--paper);
    font-size: 10.5px; font-weight: 700; letter-spacing: 1.4px;
    display: flex; align-items: center; justify-content: center;
  }

  /* back side */
  .top-band {
    position: absolute; left: 0; top: 0; width: 100%; height: 26px;
    background: linear-gradient(180deg, #000 0%, #1a1a1a 100%);
    border-bottom: 4px solid var(--brand-blue);
  }
  .help-panel {
    position: absolute; left: 12px; top: 12px; width: 336px; height: 258px;
    background: linear-gradient(180deg, #ffffff 0%, #f1f1f1 55%, #cfcfcf 100%);
    box-shadow: 2px 3px 8px rgba(0,0,0,.35);
    padding: 8px 14px 10px 14px;
  }
  .help-panel__tagline {
    font-size: 14px; font-weight: 900; font-style: italic; color: var(--brand-blue);
    line-height: 1.12; margin-bottom: 8px;
  }
  .help-panel__title { font-size: 17px; font-weight: 700; color: var(--ink); margin-bottom: 4px; }
  .help-panel p { font-size: 8.4px; line-height: 1.34; color: #333; margin-bottom: 8px; }

  .contact-ribbon { position: absolute; left: 0; top: 296px; width: 290px; height: 62px; }
  .contact-back {
    position: absolute; left: 14px; top: 300px;
    color: var(--paper); font-weight: 900; font-style: italic; line-height: 1.25;
  }
  .contact-back__phone { font-size: 14px; }
  .contact-back__url { font-size: 16px; }
</style>
</head>
<body>
<main class="stage">

  <!-- Side 1 -->
  <section class="postcard postcard--front" aria-label="Postcard front">
    <div class="backdrop backdrop--front" role="img" aria-label="White brick wall room with a black arc floor lamp lighting the wall"></div>
    <div class="lamp-area" role="img" aria-label="Arc floor lamp with black shade"></div>

    <div class="brand brand--front">Clearwater<br>Lantern Group</div>

    <svg class="bubble" viewBox="0 0 200 100" aria-hidden="true">
      <path d="M100 4 C160 4 196 22 196 46 C196 70 160 88 100 88 C88 88 76 87 66 85 L30 98 L44 80 C20 72 4 60 4 46 C4 22 40 4 100 4 Z"
            fill="#ffffff" stroke="#bdbdbd" stroke-width="1.5"/>
    </svg>
    <p class="bubble__text"><em>VISIT US</em> online to learn more about out services, check out case studies and read about ourexciting partnerships.</p>

    <svg class="about-banner" viewBox="0 0 408 156" aria-hidden="true">
      <defs>
        <linearGradient id="bannerBlue" x1="0" y1="0" x2="0" y2="1">
          <stop offset="0" stop-color="#2f86dd"/>
          <stop offset="1" stop-color="#0d3f8f"/>
        </linearGradient>
      </defs>
      <path d="M0 18 C90 2 180 28 270 10 C330 0 380 6 408 12 L398 140 C330 126 260 154 170 142 C100 132 40 146 10 150 Z"
            fill="url(#bannerBlue)" stroke="#ffffff" stroke-width="3"/>
    </svg>
    <div class="about">
      <h2 class="about__title">About my company:</h2>
      <p class="about__body">Clearwater Lantern Group is a new breed of marketing consulting agency built for the next frontier of consumer learning. Social interaction will be at the heart of great insights going forward – in how consumers engage with brands and in how organizations socialize what they learn to gain competitive advantage. By fusing innovative insights techniques, technology and compelling graphic design-based reporting, we ensure results get noticed and makean impact.</p>
    </div>

    <div class="contact-front">
      <div>Phone: 518-732-6148</div>
      <div>Email: morgan@clearwater-lantern.com</div>
    </div>
    <p class="launch-note">Visit our newly launched website to learn how and get in touch.</p>
    <div class="url-bar">www.clearwater-lantern.com</div>
  </section>

  <!-- Side 2 -->
  <section class="postcard postcard--back" aria-label="Postcard back">
    <div class="backdrop backdrop--back" role="img" aria-label="Whitewashed brick wall and pale concrete floor"></div>
    <div class="top-band"></div>

    <article class="help-panel">
      <p class="help-panel__tagline">A leading-edge marketing partnership<br>that really works.</p>
      <h2 class="help-panel__title">How we can help...</h2>
      <p>Think of us as your go-to resource for identifying and incorporating the most innovative and exciting techniques into your research programs. We carefully curate and develop close partnerships with the best of the best - from online qualitative research and mobile ethnography to social media listening and fresh takes on concept testing, we can guide the way.</p>
      <p>Plus, we believe that socializing consumer learning is just as critical as gathering it.By taking insights deliverables to the next level – through info-graphics, videos, magazines,interactive profiles and so much more – we are getting stakeholders excited to engage with research and inspired to take action because of it. It’s a new way to look at insights from a new type of partner. And, it’s a new way to get the most from your research dollars.</p>
    </article>

    <svg class="contact-ribbon" viewBox="0 0 290 62" aria-hidden="true">
      <defs>
        <linearGradient id="ribbonBlue" x1="0" y1="0" x2="0" y2="1">
          <stop offset="0" stop-color="#2a7fd6"/>
          <stop offset="1" stop-color="#0d3f8f"/>
        </linearGradient>
      </defs>
      <path d="M0 0 L268 6 L290 34 L262 62 L0 58 Z" fill="url(#ribbonBlue)"/>
    </svg>
    <div class="contact-back">
      <div class="contact-back__phone">Phone: 518-732-6148</div>
      <div class="contact-back__url">www.clearwater-lantern.com</div>
    </div>

    <div class="brand brand--back">Clearwater<br>Lantern Group</div>
  </section>

</main>
</body>
</html>
```